Poster Design Project

We are a pizzeria based in Sydney CBD. Please see attached file for new website, do not use the current website look to make your graphic design.

We want to run a promotional campaign called " Rustico Rush".

Rustico Rush
$9 Pizza

Crispy & fresh dough topped with mouth watering mozzarella cheese, sprinkled with oregano and finished with fresh basil.

takeaway & eat in only
Medium Pizza Only (11 inch)

Target Market(s)

It is the lunch crowd in sydney cbd, predominately male but some female too. targeting the office workers.

Industry/Entity Type

Graphic Design

Requirements
Must have
• We are an Italian Pizzeria, so we would like an italian look and feel
our unique advantage is authentic and delicious thin crispy pizza
we want a nostalgic look and feel
some examples are attached of colours and style we like
Nice to have
• I can send you via email files to show you what the new website will look like

```html
<!DOCTYPE html>
<html lang="en">
<head>
<meta charset="utf-8">
<title>Rustico Rush – $9 Pizza</title>
<link href="https://fonts.googleapis.com/css2?family=Alfa+Slab+One&family=Anton&family=Oleo+Script:wght@700&display=swap" rel="stylesheet">
<style>
  :root {
    --flag-green: #1f8a3c;
    --flag-white: #f4f2ec;
    --flag-red: #d8322a;
    --ink: #111111;
    --paper-light: #d9c69a;
    --paper-dark: #a88a55;
    --promo-red: #d4202a;
    --tape: rgba(235, 228, 210, 0.55);
    --footer-bg: #000000;
    --footer-text: #ffffff;
  }
  * { margin: 0; padding: 0; box-sizing: border-box; }
  html, body { width: 933px; height: 1200px; overflow: hidden; background: #ffffff; }
  .poster { position: relative; width: 933px; height: 1200px; overflow: hidden; background: var(--flag-white); }

  .flag { position: absolute; left: 0; top: 0; width: 933px; height: 955px; }
  .flag__green { position: absolute; left: 0; top: 0; width: 225px; height: 100%;
    background: linear-gradient(90deg, var(--flag-green) 80%, rgba(31,138,60,0.6) 92%, rgba(31,138,60,0)); }
  .flag__red { position: absolute; right: 0; top: 0; width: 300px; height: 100%;
    background: linear-gradient(270deg, var(--flag-red) 82%, rgba(216,50,42,0.6) 93%, rgba(216,50,42,0)); }

  .campaign-title { position: absolute; left: 40px; top: 14px; font-family: "Alfa Slab One", serif;
    font-size: 60px; line-height: 64px; letter-spacing: 2px; color: var(--ink); text-transform: uppercase; }

  .promo-card { position: absolute; left: 170px; top: 170px; width: 500px; height: 810px;
    transform: rotate(-5deg); transform-origin: center;
    background: radial-gradient(ellipse at 40% 30%, var(--paper-light), var(--paper-dark));
    border-radius: 18px; box-shadow: 6px 10px 22px rgba(0,0,0,0.35); }

  .tape { position: absolute; width: 120px; height: 44px; background: var(--tape); }
  .tape--top-left { left: 165px; top: 185px; transform: rotate(-42deg); }
  .tape--top-right { left: 610px; top: 190px; transform: rotate(48deg); }
  .tape--bottom-left { left: 95px; top: 860px; transform: rotate(55deg); }
  .tape--bottom-right { left: 560px; top: 930px; transform: rotate(-40deg); }

  .price { position: absolute; left: 290px; top: 140px; transform: rotate(-6deg);
    font-family: "Anton", sans-serif; color: var(--promo-red); text-align: center; line-height: 0.95;
    -webkit-text-stroke: 3px #ffffff; paint-order: stroke fill;
    text-shadow: 3px 4px 6px rgba(0,0,0,0.35); }
  .price__amount { display: block; font-size: 130px; }
  .price__item { display: block; font-size: 120px; margin-left: -60px; letter-spacing: 2px; }

  .description { position: absolute; left: 215px; top: 420px; width: 460px; transform: rotate(8deg);
    font-family: "Oleo Script", cursive; font-weight: 700; font-size: 25px; line-height: 29px;
    color: var(--ink); text-align: center; }

  .pizza-photo { position: absolute; left: 140px; top: 575px; width: 640px; height: 300px; }

  .footer { position: absolute; left: 0; top: 955px; width: 933px; height: 245px; background: var(--footer-bg); color: var(--footer-text); }
  .footer__terms { position: absolute; left: 54px; top: 50px; font-family: "Oleo Script", cursive; font-weight: 700;
    font-size: 29px; line-height: 44px; }
  .footer__web { position: absolute; left: 58px; top: 180px; font-family: "Oleo Script", cursive; font-weight: 700;
    font-size: 20px; letter-spacing: 13px; }
  .footer__brand { position: absolute; left: 668px; top: 110px; font-family: "Oleo Script", cursive; font-weight: 700;
    font-size: 40px; color: var(--footer-text); }
</style>
</head>
<body>
<main class="poster">
  <div class="flag" aria-hidden="true">
    <div class="flag__green"></div>
    <div class="flag__red"></div>
  </div>

  <h1 class="campaign-title">Rustico<br>Rush</h1>

  <div class="promo-card" aria-hidden="true"></div>

  <div class="price">
    <span class="price__amount">$9</span>
    <span class="price__item">PIZZA</span>
  </div>

  <p class="description">Crispy &amp; fresh dough topped with mouth watering mozzarella cheese, sprinkled with oregano and finished with fresh basil.</p>

  <svg class="pizza-photo" role="img" aria-label="Photo of a margherita pizza with a basil leaf on a round wooden serving board" viewBox="0 0 640 300">
    <defs>
      <radialGradient id="pizzaTone" cx="50%" cy="45%" r="55%">
        <stop offset="0" stop-color="#e39a3a"/>
        <stop offset="0.7" stop-color="#c4602a"/>
        <stop offset="1" stop-color="#d9a35c"/>
      </radialGradient>
      <linearGradient id="boardTone" x1="0" y1="0" x2="1" y2="1">
        <stop offset="0" stop-color="#c88a4a"/>
        <stop offset="1" stop-color="#8f5526"/>
      </linearGradient>
    </defs>
    <ellipse cx="300" cy="150" rx="300" ry="140" fill="url(#boardTone)"/>
    <ellipse cx="295" cy="140" rx="250" ry="112" fill="url(#pizzaTone)"/>
  </svg>

  <div class="tape tape--top-left" aria-hidden="true"></div>
  <div class="tape tape--top-right" aria-hidden="true"></div>
  <div class="tape tape--bottom-left" aria-hidden="true"></div>
  <div class="tape tape--bottom-right" aria-hidden="true"></div>

  <footer class="footer">
    <p class="footer__terms">Takeaway &amp; Eat In<br>Medium Pizza Only (11 inch)</p>
    <p class="footer__web">www.fornorustico.com.au</p>
    <p class="footer__brand">Forno Rustico</p>
  </footer>
</main>
</body>
</html>
```